Business Card Design

The Wren Lodge Motel is the most centrally located motel in Grafton.
We are the only family owned motel in Grafton.
Our colour scheme is blue, whiteand black.
Updates

I have uploaded a photo of our new rooms and the logo for you to use Thanks. Looking good

Industry/Entity Type

Motel

Contact Information for Business Card

The Wren Lodge Motel
Colin & Maree Tulloch
Owner/Operators
14-16 Barwell Road, Grafton NSW 2460
Ph: 02 6613 4879
Email: thewrenlodgemotel@mailbay.example
reception@wrenlodgemotel.example
www.wrenlodgemotel.example

Colors
0392cd
0455a3

```html
<!DOCTYPE html>
<html lang="en">
<head>
<meta charset="utf-8">
<title>The Wren Lodge Motel – Business Card</title>
<link rel="stylesheet" href="https://fonts.googleapis.com/css2?family=Exo+2:wght@400;600;700&display=swap">
<style>
  :root {
    --page: #e9e9ec;
    --card: #ffffff;
    --brand-blue: #0455a3;
    --accent-blue: #0392cd;
    --deep-violet: #3a3f98;
    --glow-blue: #0aa6e4;
    --ink: #1b1b1b;
    --white: #ffffff;
  }
  * { box-sizing: border-box; margin: 0; padding: 0; }
  html, body {
    width: 1200px; height: 900px; overflow: hidden;
    background: var(--page);
    font-family: "Exo 2", sans-serif;
  }
  .canvas { position: relative; width: 1200px; height: 900px; }
  .card {
    position: absolute; left: 250px; width: 700px; height: 400px;
    background: var(--card);
    box-shadow: 0 6px 18px rgba(0,0,0,0.18);
    overflow: hidden;
  }
  .card--front { top: 40px; }
  .card--back { top: 470px; }

  .contact-panel {
    position: absolute; top: 0; right: 0; bottom: 0; left: 400px;
    background: radial-gradient(ellipse at 50% 55%, var(--glow-blue) 0%, #1f6cc3 50%, var(--deep-violet) 100%);
  }

  .holder { position: absolute; left: 44px; top: 48px; }
  .holder__name {
    color: var(--accent-blue); font-size: 22px; font-weight: 400;
    letter-spacing: 2px; text-transform: uppercase;
  }
  .holder__role { color: var(--ink); font-size: 14px; margin-top: 4px; letter-spacing: 0.5px; }

  .wordmark {
    position: absolute; display: flex; align-items: center; gap: 12px;
    color: var(--brand-blue); font-weight: 700; line-height: 1.05;
    white-space: nowrap;
  }
  .wordmark__dot { border-radius: 50%; background: var(--brand-blue); flex: none; }
  .card--front .wordmark { left: 44px; bottom: 44px; font-size: 26px; }
  .card--front .wordmark__dot { width: 26px; height: 26px; }
  .card--back .wordmark { left: 50%; top: 50%; transform: translate(-50%, -50%); font-size: 46px; }
  .card--back .wordmark__dot { width: 46px; height: 46px; }

  .contacts {
    position: absolute; right: 28px; top: 34px; list-style: none;
    color: var(--white); font-size: 12px; letter-spacing: 0.6px;
    text-align: right;
  }
  .contacts li { display: flex; justify-content: flex-end; align-items: center; gap: 10px; height: 27px; white-space: nowrap; }
  .contacts svg { width: 14px; height: 14px; flex: none; }

  .address {
    position: absolute; right: 28px; bottom: 26px;
    color: var(--white); font-size: 12px; letter-spacing: 0.5px; white-space: nowrap;
  }
</style>
</head>
<body>
<main class="canvas">

  <section class="card card--front" aria-label="Business card front">
    <div class="contact-panel" role="img" aria-label="Blue gradient contact panel"></div>

    <div class="holder">
      <p class="holder__name">Colin &amp; Maree Tulloch</p>
      <p class="holder__role">Owner/Operators</p>
    </div>

    <div class="wordmark"><span class="wordmark__dot"></span><span>The Wren Lodge Motel</span></div>

    <ul class="contacts">
      <li>02 6613 4879
        <svg viewBox="0 0 16 16"><path d="M3 1.5 5.5 1l1.5 3.5-1.8 1.2a8 8 0 0 0 5.1 5.1L11.5 9 15 10.5 14.5 13A2 2 0 0 1 12.5 15 11.5 11.5 0 0 1 1 3.5 2 2 0 0 1 3 1.5z" fill="#fff"/></svg></li>
      <li>02 6613 4879
        <svg viewBox="0 0 16 16"><rect x="4" y="1" width="8" height="14" rx="1.5" fill="none" stroke="#fff" stroke-width="1.5"/><circle cx="8" cy="12.5" r="0.9" fill="#fff"/></svg></li>
      <li>02 6613 4879
        <svg viewBox="0 0 16 16"><rect x="2" y="6" width="12" height="8" rx="1" fill="#fff"/><rect x="4.5" y="1.5" width="7" height="5" fill="none" stroke="#fff" stroke-width="1.3"/></svg></li>
      <li>thewrenlodgemotel@mailbay.example
        <svg viewBox="0 0 16 16"><rect x="1.5" y="3.5" width="13" height="9" fill="none" stroke="#fff" stroke-width="1.4"/><path d="M1.5 3.5 8 9l6.5-5.5" fill="none" stroke="#fff" stroke-width="1.4"/></svg></li>
      <li>www.wrenlodgemotel.example
        <svg viewBox="0 0 16 16"><circle cx="8" cy="8" r="6.5" fill="none" stroke="#fff" stroke-width="1.3"/><ellipse cx="8" cy="8" rx="2.8" ry="6.5" fill="none" stroke="#fff" stroke-width="1.1"/><path d="M1.5 8h13" stroke="#fff" stroke-width="1.1"/></svg></li>
    </ul>

    <p class="address">14-16 Barwell Road, Grafton NSW 2460</p>
  </section>

  <section class="card card--back" aria-label="Business card back">
    <div class="wordmark"><span class="wordmark__dot"></span><span>The Wren Lodge Motel</span></div>
  </section>

</main>
</body>
</html>
```